Home Health Company Needs a Corporate Identity Package

We need a corporate identity package (see what it should include below) for a home health care company. The design should be professional, uncluttered, simple and created in Publisher (so that we can edit the design in the future, if necessary. )
We need the following created:
-Presentation folder
-Business card template (color, double sided)
-Letterhead
-Stationary
-postcard sized marketing piece (5.5" x 8.5", color, double sided)

Target Market(s)

We are in the business of supplying personal care aids for in home care. Our services are directed towards older, retired individuals with some disability or illness. However, we will be marketing to the children or relatives of our in home clients. We want our logo to emphasize our reliability and personalized services.

Industry/Entity Type

Home Health Care

Requirements
Must have
• The design should be professional, uncluttered, simple and created in Publisher (so that we can edit the design in the future, if necessary. )

```html
<!DOCTYPE html>
<html lang="en">
<head>
<meta charset="utf-8">
<title>Brightpath Home Care – Envelope</title>
<link rel="stylesheet" href="https://fonts.googleapis.com/css2?family=Open+Sans:wght@400;600;700&display=swap">
<style>
  :root {
    --backdrop: #e9e9ea;
    --paper: #ffffff;
    --brand-blue: #4cc8f0;
    --brand-grey: #5d5e62;
    --text-grey: #6a6b6f;
    --faint-grey: #efefef;
  }
  html, body {
    margin: 0;
    width: 1200px;
    height: 892px;
    overflow: hidden;
    background: var(--backdrop);
    font-family: "Open Sans", Arial, sans-serif;
  }
  .canvas {
    position: relative;
    width: 1200px;
    height: 892px;
  }
  .envelope {
    position: absolute;
    width: 720px;
    height: 340px;
    background: var(--paper);
    overflow: hidden;
    box-shadow: 0 2px 6px rgba(0,0,0,0.12);
  }
  /* Back of the envelope with flap band */
  .envelope--back {
    left: 440px;
    top: 50px;
  }
  .envelope--back .flap-band {
    position: absolute;
    left: 0;
    top: 0;
    width: 720px;
    height: 120px;
  }
  .envelope--back .flap-mark {
    position: absolute;
    left: 340px;
    top: 135px;
    width: 40px;
    height: 40px;
    border-radius: 50%;
    background: #c9cacc;
  }
  /* Front of the envelope */
  .envelope--front {
    left: 40px;
    top: 480px;
  }
  .brand {
    position: absolute;
    left: 48px;
    top: 44px;
    display: flex;
    align-items: center;
    gap: 14px;
  }
  .brand__dot {
    width: 34px;
    height: 34px;
    border-radius: 50%;
    background: var(--brand-blue);
  }
  .brand__name {
    font-weight: 700;
    font-size: 34px;
    line-height: 1;
    color: var(--brand-grey);
    letter-spacing: -0.5px;
  }
  .front-watermark {
    position: absolute;
    right: -90px;
    bottom: -150px;
    width: 340px;
    height: 340px;
    border-radius: 50%;
    border: 26px solid var(--faint-grey);
    box-sizing: border-box;
  }
  .return-address {
    position: absolute;
    left: 48px;
    bottom: 52px;
    margin: 0;
    font-size: 11px;
    font-weight: 600;
    color: var(--text-grey);
    letter-spacing: 0.1px;
  }
  .front-band {
    position: absolute;
    left: 0;
    bottom: 0;
    width: 452px;
    height: 26px;
    background: var(--brand-blue);
  }
  .front-block {
    position: absolute;
    left: 458px;
    bottom: 0;
    width: 262px;
    height: 42px;
    background: var(--brand-grey);
  }
</style>
</head>
<body>
<main class="canvas">
  <section class="envelope envelope--back" aria-label="Envelope back">
    <svg class="flap-band" viewBox="0 0 720 120" aria-hidden="true">
      <path d="M0 0 H720 V120 Q720 96 696 96 H690 Q690 60 666 60 H48 Q24 60 24 36 V0 Z" fill="var(--brand-blue)"/>
      <path d="M0 0 H720 V60 H0 Z" fill="var(--brand-blue)"/>
      <path d="M0 60 H690 Q720 60 720 90 V120 Q716 60 690 60 Z" fill="var(--brand-blue)"/>
    </svg>
    <div class="flap-mark" aria-hidden="true"></div>
  </section>

  <section class="envelope envelope--front" aria-label="Envelope front">
    <div class="front-watermark" aria-hidden="true"></div>
    <div class="brand">
      <span class="brand__dot" aria-hidden="true"></span>
      <span class="brand__name">Brightpath Home Care</span>
    </div>
    <p class="return-address">Suite 210-Second Floor, Maple Court Tower, Lakeview-411014, Pune, India</p>
    <div class="front-band"></div>
    <div class="front-block"></div>
  </section>
</main>
</body>
</html>
```